Visitenkarten-Design für Immobilien-Unternehmen
Designer ist sehr bemüht und die Änderungswünsche wurden rasch bearbeitet. Auch wurde im Nachhinein noch mein Wunsch auf Adaptierung zu einem Lackdruck bearbeitet und gesendet. Ich bin mit der Abwicklung vollkommen zufrieden - Vielen Dank
Zielgruppe
Die TOLU Immobilien GmbH ist eine durch Ing. Kilian Frühwald inhabergeführte Gesellschaft, welche sich schwerpunktmäßig mit Immobilieninvestitionen sowie Beteiligungen im Bereich von Wohn- und Gewerbeimmobilien beschäftigt. Das Unternehmen kauft, hält, vermietet und verkauft Liegenschaften aller Art, mit dem Fokus auf Gewerbe- und Wohnimmobilien. Zielgruppe sind Personen, welche Immobilien verkaufen möchten - wir betreiben nur eigene Vermögensverwaltung
siehe: www.tolu-immobilien.at
Aufgabenstellung
schlicht und einfach gehalten - weniger ist mehr - nur die wichtigsten Informationen auf der Visitenkarte.
siehe Homepage: www.tolu-immobilien.at

```html
<!DOCTYPE html>
<html lang="de">
<head>
<meta charset="utf-8">
<title>TOLU Immobilien GmbH – Visitenkarte</title>
<link rel="stylesheet" href="https://fonts.googleapis.com/css2?family=Open+Sans:wght@300;400;600&display=swap">
<style>
  :root {
    --stage: #e6e6e4;
    --card: #2b2b2c;
    --card-deep: #232324;
    --ink: #f2f2f2;
    --ink-soft: #b9b9b9;
    --rule: #8a8a8a;
    --pattern-a: #2e2e2f;
    --pattern-b: #262627;
  }
  * { margin: 0; padding: 0; box-sizing: border-box; }
  html, body { width: 1200px; height: 898px; overflow: hidden; }
  body {
    background: var(--stage);
    font-family: "Open Sans", Arial, sans-serif;
    color: var(--ink);
    position: relative;
  }
  .card {
    position: absolute;
    top: 294px;
    width: 510px;
    height: 310px;
    border-radius: 22px;
    background: var(--card);
    box-shadow: 0 14px 30px rgba(0,0,0,.25);
    overflow: hidden;
  }
  .card--front { left: 70px; }
  .card--back { left: 620px; background: var(--card-deep); }

  .person { position: absolute; left: 34px; top: 34px; }
  .person__name { font-size: 14px; font-weight: 600; letter-spacing: .08em; }
  .person__role { font-size: 10px; font-weight: 400; color: var(--ink-soft); margin-top: 2px; }

  .contact { position: absolute; left: 34px; top: 92px; list-style: none; }
  .contact__item {
    display: flex; align-items: center; gap: 8px;
    font-size: 10.5px; color: var(--ink-soft); line-height: 18px;
  }
  .contact__icon { width: 10px; height: 10px; flex: none; }
  .contact__rule {
    position: absolute; left: 34px; top: 176px; width: 190px;
    border-top: 1px solid var(--rule);
  }

  .brand { position: absolute; right: 34px; top: 104px; text-align: right; }
  .brand__name {
    font-size: 66px; font-weight: 400; line-height: 1; letter-spacing: .02em; color: var(--ink);
  }
  .brand__legal {
    font-size: 14px; font-weight: 400; letter-spacing: .16em; color: var(--ink); margin-top: 4px;
  }
  .brand__rule {
    position: absolute; right: 34px; top: 212px; width: 250px;
    border-top: 1px solid var(--rule);
  }
  .address {
    position: absolute; right: 34px; top: 226px; text-align: right;
    font-size: 12px; line-height: 18px; color: var(--ink);
  }

  .back__pattern {
    position: absolute; inset: 0;
    background: linear-gradient(160deg, var(--pattern-a), var(--pattern-b));
  }
  .back__brand { position: absolute; right: 40px; bottom: 48px; text-align: right; }
  .back__name { font-size: 26px; font-weight: 400; line-height: 1; color: var(--ink); }
  .back__legal { font-size: 6.5px; letter-spacing: .18em; color: var(--ink); margin-top: 3px; }
</style>
</head>
<body>
  <section class="card card--front" aria-label="Vorderseite der Visitenkarte">
    <div class="person">
      <p class="person__name">LUKAS HARTL</p>
      <p class="person__role">Director</p>
    </div>
    <ul class="contact">
      <li class="contact__item">
        <svg class="contact__icon" viewBox="0 0 10 10"><path d="M2 1l2 2-1 1.2a6 6 0 0 0 2.8 2.8L7 6l2 2-1.3 1.3C4.6 9 1 5.4.7 2.3z" fill="#b9b9b9"/></svg>
        +43 664 987 21 45
      </li>
      <li class="contact__item">
        <svg class="contact__icon" viewBox="0 0 10 10"><rect x=".5" y="2" width="9" height="6" fill="none" stroke="#b9b9b9"/><path d="M.5 2L5 5.5 9.5 2" fill="none" stroke="#b9b9b9"/></svg>
        office@tolu-immobilien.at
      </li>
      <li class="contact__item">
        <svg class="contact__icon" viewBox="0 0 10 10"><circle cx="5" cy="5" r="4.3" fill="none" stroke="#b9b9b9"/><ellipse cx="5" cy="5" rx="1.8" ry="4.3" fill="none" stroke="#b9b9b9"/><path d="M.7 5h8.6" stroke="#b9b9b9"/></svg>
        www.tolu-immobilien.at
      </li>
    </ul>
    <div class="contact__rule"></div>

    <div class="brand">
      <p class="brand__name">TOLU</p>
      <p class="brand__legal">IMMOBILIEN GMBH</p>
    </div>
    <div class="brand__rule"></div>
    <address class="address" style="font-style:normal">
      Lindenweg 14/3 8010<br>Graz Austria
    </address>
  </section>

  <section class="card card--back" aria-label="Rückseite der Visitenkarte">
    <div class="back__pattern" role="img" aria-label="Dezentes Lackdruck-Muster aus wiederholtem Firmennamen, Ton in Ton"></div>
    <div class="back__brand">
      <p class="back__name">TOLU</p>
      <p class="back__legal">IMMOBILIEN GMBH</p>
    </div>
  </section>
</body>
</html>
```